依頼詳細
キャッチコピーは以下になります。変わる可能性がありますので文字修正は簡単にできるようにお願いします。
PSDファイル、高解像度JPG、PNG形式、全てのファイル納品でお願いいたします。
記載項目
———————————————————
仕事もプライベートも充実する
生活をしたいあなたに

あなたの趣味・資格がお金に変わる
無理しなくてもできる

オーダーメイド
複業のはじめ方

もうひとつのキャリアで
複数の収入を得て
普段よりリッチな生活が
できる方法を公開

自宅で聴ける少人数制の
オンラインセミナーを
期間限定で無料で開催中

<オンラインセミナーに申し込む>ボタン
ご自宅で受講することができます
————————————————————

自由な発想でデザインをお願いします。
サイズ
• 2001(縦) x 1125(横)
希望イメージ
シンプル 複雑
単色 カラフル
暗い 明るい
日常 高級
遊び心 厳粛
未来的 伝統的
女性的 男性的
希望する色
淡い色が希望になります
納品ファイル
• 高解像度JPG (.jpg)
• フォトショップ形式 (.psd)
• PNG形式 (.png)
補足説明
<ターゲット>
30代の女性OL
ビジネス初心者の方
これから自分でスキルをつけて会社とは別に収入を得たい方になります。
年収は250万以上の単身者になります。

<その他>
自分が好きなことができる
楽しいということがイメージできる
色調とデザインでお願いいたします。

当LPを閲覧する人の80%程度はスマホでの閲覧と想定されます。
スマホで閲覧しても、当選した後に別途追加1,000円程度でPCからの閲覧でも
きれいに表示されるように縦957px×横1300pxでサイズ修正をお願いいたします。

<継続依頼>
当選者様にはそのままヘッダー以下のデザインもお願いしたいと思っています。
また本案件のコピー以外のパターンのデザインも追加発注も考えております。
価格についてはまたご相談させて頂きます。
■ 選んだ理由

女性を意識したデザインと、
文字のバランスなどを考慮して選ばせて頂きました。

■ 提案者全員のお礼・コメント

この度は当社のコンペに参加をして頂き、ありがとうございます。
今後もwebデザインのご依頼をさせて頂きますので、今後ともどうぞよろしくお願い致します。

```html
<!DOCTYPE html>
<html lang="ja">
<head>
<meta charset="UTF-8">
<title>オーダーメイド複業のはじめ方 オンラインセミナー</title>
<link href="https://fonts.googleapis.com/css2?family=M+PLUS+Rounded+1c:wght@500;700;800&family=Noto+Serif+JP:wght@500;600;700&family=Noto+Sans+JP:wght@500;700&display=swap" rel="stylesheet">
<style>
  :root {
    --cream: #fff6d6;
    --pale-yellow: #fdf0c2;
    --warm-yellow: #f9d97a;
    --orange: #f29a1f;
    --orange-deep: #ee8a12;
    --ink: #4a4440;
    --white: #ffffff;
    --green: #4caf46;
    --green-dark: #3d9a38;
  }
  * { margin: 0; padding: 0; box-sizing: border-box; }
  html, body { width: 673px; height: 1200px; overflow: hidden; background: var(--pale-yellow); }
  .banner {
    position: relative; width: 673px; height: 1200px; overflow: hidden;
    background: var(--pale-yellow);
    font-family: "Noto Sans JP", sans-serif; color: var(--ink);
  }
  .banner > * { position: absolute; }

  .top-band {
    left: 0; top: 0; width: 673px; height: 168px; background: var(--cream);
    display: flex; flex-direction: column; align-items: center; justify-content: center; gap: 6px;
    font-family: "M PLUS Rounded 1c", sans-serif; font-weight: 800;
  }
  .top-band .lead-1 { font-size: 44px; letter-spacing: 1px; }
  .top-band .lead-2 { font-size: 40px; letter-spacing: 1px; }
  .accent { color: var(--orange); }

  .title-block {
    left: 0; top: 168px; width: 673px; height: 302px; background: var(--white);
    text-align: center; font-family: "Noto Serif JP", serif;
  }
  .title-block .sub { font-size: 30px; font-weight: 600; line-height: 44px; letter-spacing: 1px; }
  .title-block .sub:first-child { margin-top: 12px; }
  .title-block .main {
    color: var(--orange-deep); font-weight: 700; font-size: 72px; line-height: 84px; letter-spacing: 2px;
  }

  .visual {
    left: 0; top: 470px; width: 673px; height: 560px;
    background: linear-gradient(90deg, var(--warm-yellow) 0%, #fbe6a6 45%, #f4efe8 70%, #eee7df 100%);
  }

  .bubble {
    left: 34px; top: 492px; width: 318px; height: 248px;
    border: 3px solid var(--orange); border-radius: 50%; background: var(--white);
    display: flex; align-items: center; justify-content: center; text-align: center;
    font-family: "M PLUS Rounded 1c", sans-serif; font-weight: 700;
    font-size: 26px; line-height: 38px;
  }
  .bubble-tail { left: 300px; top: 690px; }

  .invite { left: 40px; top: 822px; font-family: "Noto Serif JP", serif; font-weight: 700; font-size: 33px; }
  .invite .line { display: table; background: var(--white); padding: 2px 8px; margin-bottom: 6px; line-height: 44px; }
  .invite .highlight { background: var(--orange); color: var(--white); padding: 0 2px; }

  .cta {
    left: 56px; top: 1050px; width: 561px; height: 62px;
    background: linear-gradient(180deg, var(--green), var(--green-dark));
    color: var(--white); font-weight: 500; font-size: 29px; letter-spacing: 1px;
    display: flex; align-items: center; justify-content: center; gap: 16px;
    box-shadow: 0 3px 0 #2f7f2b;
  }
  .note {
    left: 0; top: 1140px; width: 673px; text-align: center;
    color: var(--orange-deep); font-family: "Noto Serif JP", serif; font-weight: 700; font-size: 33px;
  }
</style>
</head>
<body>
<div class="banner">
  <header class="top-band">
    <p class="lead-1"><span class="accent">仕事</span>も<span class="accent">プライベート</span>も充実する</p>
    <p class="lead-2">生活をしたいあなたに</p>
  </header>

  <section class="title-block">
    <p class="sub">あなたの趣味・資格がお金に変わる</p>
    <p class="sub">無理しなくてもできる</p>
    <h1 class="main">オーダーメイド<br>複業のはじめ方</h1>
  </section>

  <div class="visual" role="img" aria-label="自宅でノートパソコンに向かって微笑む女性の写真"></div>

  <svg class="bubble-tail" width="60" height="50" viewBox="0 0 60 50" aria-hidden="true">
    <path d="M2 6 L56 44 L18 2 Z" fill="#ffffff" stroke="#f29a1f" stroke-width="3" stroke-linejoin="round"/>
  </svg>
  <div class="bubble">
    <p>もうひとつのキャリアで<br>複数の収入を得て<br>普段よりリッチな生活が<br>できる方法を公開</p>
  </div>

  <div class="invite">
    <p class="line">自宅で聴ける少人数制の</p>
    <p class="line">オンラインセミナーを</p>
    <p class="line"><span class="highlight">期間限定</span>で無料で開催中</p>
  </div>

  <a class="cta">オンラインセミナーに申し込む
    <svg width="16" height="18" viewBox="0 0 16 18" aria-hidden="true"><path d="M0 0 L16 9 L0 18 Z" fill="#ffffff"/></svg>
  </a>

  <p class="note">ご自宅で受講することができます</p>
</div>
</body>
</html>
```